Pediatric Pelvic Health Brochure

Looking to design a brochure for Marlow Crest's pelvic health program. I can provide imagery once I see the layout. Our website is marlowcrestpt.example so the look should reflect that

If you see PDF titled blue and word doc you will see what we provided as thoguhts.

Target Market(s)

parents of children

Industry/Entity Type

Health And Wellness

Font styles to use
Serif

Requirements
Must have
• clear call outs - easy to read with copy,
Should not have
• not look bland or dated

```html
<!DOCTYPE html>
<html lang="en">
<head>
<meta charset="utf-8">
<title>Marlow Crest – Pediatric Pelvic Health Brochure</title>
<link rel="stylesheet" href="https://fonts.googleapis.com/css2?family=Arimo:wght@400;700&family=Tinos:wght@400;700&display=swap">
<style>
:root{
  --navy:#1c3d92;
  --navy-deep:#14307a;
  --cyan:#14b6ea;
  --cyan-soft:#3cc6f0;
  --ink:#4a4f5c;
  --paper:#ffffff;
  --paper-warm:#f6f4f1;
  --backdrop:#cfd0d3;
  --photo-a:#c9d3df;
  --photo-b:#e9e3dc;
}
*{box-sizing:border-box;margin:0;padding:0}
html,body{width:796px;height:1200px;overflow:hidden;background:var(--backdrop)}
.stage{position:absolute;left:0;top:0;width:980px;height:1477px;transform:scale(.81224);transform-origin:0 0;font-family:"Arimo",Arial,sans-serif;color:var(--ink)}
.sheet{position:absolute;left:97px;width:800px;height:622px;box-shadow:0 10px 14px rgba(0,0,0,.22)}
.sheet--outside{top:72px}
.sheet--inside{top:740px}
.panel{position:absolute;top:0;height:622px;overflow:hidden}
.panel--light{background:linear-gradient(180deg,var(--paper) 0%,var(--paper-warm) 100%)}
.panel--dark{background:linear-gradient(180deg,var(--navy) 0%,var(--navy-deep) 100%);color:#fff}
.photo{position:absolute;display:block}
.serif-head{font-family:"Tinos","Times New Roman",serif;font-weight:400;letter-spacing:.5px;text-transform:uppercase}
.body-copy{font-size:11.3px;line-height:15px;text-align:justify}
.body-copy p{margin-bottom:15px}
.pill{position:absolute;height:22px;border-radius:11px;display:flex;align-items:center;justify-content:center;gap:7px;font-size:12.5px;box-shadow:0 2px 3px rgba(0,0,0,.25)}
.pill svg{width:13px;height:13px}
.pill--navy{background:var(--navy);color:#fff}
.pill--cyan{background:var(--cyan);color:#fff}
.pill--white{background:#fff;color:var(--navy)}
.big-title{font-weight:700;font-size:26px;line-height:29px;letter-spacing:1px;text-align:center;color:#fff}
.subtitle{font-family:"Tinos","Times New Roman",serif;font-size:13px;line-height:19px;letter-spacing:.6px;text-transform:uppercase;color:var(--cyan-soft);text-align:center}

/* diagnoses list */
.diagnoses{position:absolute;left:16px;top:210px;width:238px;list-style:none}
.diagnoses li{position:relative;padding:0 0 4px 16px;margin-bottom:5px;font-size:10.3px;line-height:11px;border-bottom:1px dotted #c4c7cf}
.diagnoses li::before{content:"";position:absolute;left:1px;top:2px;width:7px;height:7px;border-radius:50%;background:var(--cyan);box-shadow:inset 0 0 0 2px #bfeaf9}
.diagnoses li:last-child{border-bottom:none}

/* contact */
.contact-head{position:absolute;left:0;right:0;top:333px;text-align:center;font-weight:700;font-size:21px;letter-spacing:.5px}
.contact-rule{position:absolute;left:56px;right:56px;top:366px;height:1px;background:rgba(255,255,255,.4)}
.contact-text{position:absolute;left:20px;right:20px;text-align:center;font-size:11px;line-height:14px}
.contact-icon{position:absolute;left:50%;transform:translateX(-50%);width:20px;height:20px}

/* brand */
.brand{position:absolute;left:24px;top:34px;display:flex;align-items:center;gap:8px}
.brand-square{width:46px;height:46px;background:var(--navy)}
.brand-name{font-family:"Tinos","Times New Roman",serif;font-size:32px;line-height:32px;color:var(--navy)}

/* testimonial */
.review{position:absolute;left:20px;top:494px;width:225px;height:82px;border:1px solid rgba(255,255,255,.7);border-radius:10px;padding:20px 10px 6px}
.review-badge{position:absolute;left:50%;top:-8px;transform:translateX(-50%);width:46px;height:18px;border-radius:3px;background:var(--navy)}
.review-badge::after{content:"";position:absolute;inset:4px 6px;border-radius:2px;background:#e7c64a}
.review p{font-size:7.6px;line-height:9.6px;font-style:italic;text-align:justify}
.bar{position:absolute;top:588px;height:20px;background:var(--cyan);color:#fff;font-size:11.5px;display:flex;align-items:center}
</style>
</head>
<body>
<div class="stage">

  <!-- OUTSIDE SHEET -->
  <section class="sheet sheet--outside">

    <!-- diagnoses panel -->
    <div class="panel panel--light" style="left:0;width:261px">
      <svg class="photo" style="left:0;top:0" width="261" height="182" role="img" aria-label="Photo: a smiling doctor examining a young girl with a stethoscope">
        <defs><linearGradient id="g1" x1="0" y1="0" x2="1" y2="1"><stop offset="0" stop-color="#e6d9cd"/><stop offset="1" stop-color="#f3ece6"/></linearGradient></defs>
        <path d="M0 0H261V176Q130 182 0 178Z" fill="url(#g1)"/>
      </svg>
      <h2 class="serif-head" style="position:absolute;left:16px;top:209px;font-size:17px;line-height:21px;color:var(--navy)">We Treat a Range<br>of Diagnoses</h2>
      <ul class="diagnoses" style="top:261px">
        <li>Constipation</li>
        <li>Increased urinary frequency</li>
        <li>Decreased urinary frequency</li>
        <li>Day-time incontinence</li>
        <li>Night-time incontinence, bed-wetting,<br>or enuresis</li>
        <li>Giggle incontinence</li>
        <li>Incontinence in the athletic female<br>child or teenager</li>
        <li>Waking up in the night to urinate or nocturia</li>
        <li>Difficulty with urination: straining, slow flow,<br>pain during or after urination</li>
        <li>Reduced sensation of bladder or bowel fullness</li>
        <li>Pain in the abdomen, bladder or lower back</li>
        <li>Fecal incontinence</li>
        <li>Treatment after pediatric pelvic surgeries</li>
      </ul>
      <div class="pill pill--navy" style="left:33px;top:580px;width:200px">
        <svg viewBox="0 0 14 14" fill="none" stroke="currentColor" stroke-width="1.2"><circle cx="7" cy="7" r="6"/><ellipse cx="7" cy="7" rx="2.6" ry="6"/><path d="M1 7h12M2 4h10M2 10h10"/></svg>
        www.marlowcrestpt.example
      </div>
    </div>

    <!-- contact panel -->
    <div class="panel panel--dark" style="left:261px;width:263px">
      <svg class="photo" style="left:67px;top:54px" width="142" height="142" role="img" aria-label="Photo: a doctor with a toddler holding a teddy bear">
        <circle cx="71" cy="71" r="69" fill="none" stroke="#2a8fd8" stroke-width="4"/>
        <circle cx="71" cy="71" r="63" fill="#dfe6ee"/>
      </svg>
      <div class="big-title" style="position:absolute;left:0;right:0;top:210px">PEDIATRIC<br>PELVIC HEALTH</div>
      <div class="subtitle" style="position:absolute;left:0;right:0;top:273px">Treating Infants, Children<br>&amp; Adolescents</div>
      <div class="contact-head">CONTACT US</div>
      <div class="contact-rule"></div>
      <p class="contact-text" style="top:378px">We offer a FREE 15 minute consultation<br>to help you determine if physical<br>therapy is right for you.</p>
      <svg class="contact-icon" style="top:437px" viewBox="0 0 20 20" fill="none" stroke="var(--cyan-soft)" stroke-width="1.4"><circle cx="10" cy="10" r="8"/><path d="M7.5 6.5l1.5 1.5-1 1.2q1 2 3 3l1.2-1 1.5 1.5-1.2 1.3q-4 -1 -6-6z" fill="var(--cyan-soft)" stroke="none"/></svg>
      <p class="contact-text" style="top:463px">555.014.2200</p>
      <svg class="contact-icon" style="top:487px" viewBox="0 0 20 20" fill="none" stroke="var(--cyan-soft)" stroke-width="1.4"><path d="M10 15s-4.5-4.5-4.5-8a4.5 4.5 0 0 1 9 0c0 3.5-4.5 8-4.5 8z"/><circle cx="10" cy="7" r="1.6"/><path d="M3 18h14"/></svg>
      <p class="contact-text" style="top:517px">120 Harbor Lane<br>Ground Floor<br>Fairview, NY 10499</p>
      <div class="pill pill--cyan" style="left:40px;top:580px;width:200px">
        <svg viewBox="0 0 14 14" fill="none" stroke="currentColor" stroke-width="1.2"><circle cx="7" cy="7" r="6"/><ellipse cx="7" cy="7" rx="2.6" ry="6"/><path d="M1 7h12M2 4h10M2 10h10"/></svg>
        www.marlowcrestpt.example
      </div>
    </div>

    <!-- cover panel -->
    <div class="panel panel--dark" style="left:524px;width:276px">
      <div style="position:absolute;left:0;top:0;width:276px;height:120px;background:var(--paper)"></div>
      <div class="brand"><span class="brand-square"></span><span class="brand-name">Marlow Crest</span></div>
      <svg class="photo" style="left:0;top:112px" width="276" height="352" role="img" aria-label="Photo: a father holding his daughter while talking with a smiling doctor">
        <defs><linearGradient id="g2" x1="0" y1="0" x2="0" y2="1"><stop offset="0" stop-color="#d7dde4"/><stop offset="1" stop-color="#b9c3cf"/></linearGradient></defs>
        <path d="M0 12Q140 -6 276 6V326Q140 326 0 346Z" fill="url(#g2)"/>
        <path d="M0 346Q140 324 276 326V338Q140 336 0 352Z" fill="var(--cyan)"/>
      </svg>
      <div class="big-title" style="position:absolute;left:0;right:0;top:477px">PEDIATRIC<br>PELVIC HEALTH</div>
      <div class="subtitle" style="position:absolute;left:0;right:0;top:544px;line-height:15px">Treating Infants, Children<br>&amp; Adolescents</div>
      <div class="pill pill--white" style="left:40px;top:580px;width:200px">
        <svg viewBox="0 0 14 14" fill="none" stroke="currentColor" stroke-width="1.2"><circle cx="7" cy="7" r="6"/><ellipse cx="7" cy="7" rx="2.6" ry="6"/><path d="M1 7h12M2 4h10M2 10h10"/></svg>
        www.marlowcrestpt.example
      </div>
    </div>
  </section>

  <!-- INSIDE SHEET -->
  <section class="sheet sheet--inside" style="left:96px;width:802px">

    <!-- we help -->
    <div class="panel panel--dark" style="left:0;width:268px">
      <h2 class="serif-head" style="position:absolute;left:25px;top:58px;font-size:19px">We Help</h2>
      <div class="body-copy" style="position:absolute;left:25px;top:93px;width:225px">
        <p>Although millions of children suffer from pelvic floor dysfunction, it often takes a long time to receive the right treatment.</p>
        <p>Typically, children are toilet trained by age 4. After age 4, bowel and bladder dysfunction is considered a major medical issue that affects the family unit.</p>
        <p>Pelvic problems in children greatly influence the quality of life, self-image, social interactions, participation in sports, etc.</p>
        <p>A pelvic physical therapist can help restore normality in bladder and bowel function and prevent the progression of problems that, if untreated, may be carried over into adult life.</p>
      </div>
      <svg class="photo" style="left:0;top:392px" width="268" height="230" role="img" aria-label="Photo: a mother holding her baby during a friendly visit with a doctor">
        <defs><linearGradient id="g3" x1="0" y1="0" x2="1" y2="0"><stop offset="0" stop-color="#e8ecf1"/><stop offset="1" stop-color="#cfd8e2"/></linearGradient></defs>
        <path d="M0 14Q150 -8 268 40V230H0Z" fill="url(#g3)"/>
        <path d="M0 4Q150 -18 268 32V40Q150 -8 0 14Z" fill="var(--cyan)"/>
      </svg>
    </div>

    <!-- we specialize -->
    <div class="panel panel--light" style="left:268px;width:263px">
      <h2 class="serif-head" style="position:absolute;left:0;right:0;top:53px;text-align:center;font-size:19px;color:var(--cyan)">We Specialize</h2>
      <div class="body-copy" style="position:absolute;left:18px;top:93px;width:225px">
        <p>Although millions of children suffer from pelvic floor dysfunction, it often takes a long time to receive the right treatment.</p>
        <p>Typically, children are toilet trained by age 4. After age 4, bowel and bladder dysfunction is considered a major medical issue that affects the family unit.</p>
      </div>
      <svg class="photo" style="left:0;top:240px" width="263" height="176" role="img" aria-label="Photo: a young boy sitting on a toilet, resting his chin on his hand">
        <rect width="263" height="176" fill="#d9e3ec"/>
      </svg>
      <div class="body-copy" style="position:absolute;left:18px;top:433px;width:225px">
        <p>Pelvic problems in children greatly influence the quality of life, self-image, social interactions, participation in sports, etc.</p>
        <p>A pelvic physical therapist can help restore normality in bladder and bowel function and prevent the progression of problems that, if untreated, may be carried over into adult life.</p>
      </div>
      <div class="bar" style="left:18px;width:245px;padding-left:20px;border-radius:10px 0 0 10px">Visit our website for more information</div>
    </div>

    <!-- we partner -->
    <div class="panel panel--dark" style="left:531px;width:271px">
      <svg class="photo" style="left:0;top:0" width="271" height="252" role="img" aria-label="Photo: a doctor gently checking a baby with a stethoscope">
        <defs><linearGradient id="g4" x1="0" y1="0" x2="1" y2="1"><stop offset="0" stop-color="#eef1f4"/><stop offset="1" stop-color="#e6d6cb"/></linearGradient></defs>
        <path d="M0 0H271V160Q190 232 0 234Z" fill="url(#g4)"/>
        <path d="M0 234Q190 232 271 160V174Q190 244 0 248Z" fill="var(--cyan)"/>
      </svg>
      <h2 class="serif-head" style="position:absolute;left:20px;top:276px;font-size:19px">We Partner</h2>
      <div class="body-copy" style="position:absolute;left:20px;top:311px;width:225px">
        <p>Pelvic dysfunction problems in children in general, and in those with neurological pathologies even more, are markedly different from those in adults.</p>
        <p>Thus a therapist needs to work with parents, teachers, and other healthcare professionals such as urologists, GI’s, pediatric physical therapists, and psychologists to provide an integrated and comprehensive plan of care.</p>
      </div>
      <div class="review">
        <span class="review-badge"></span>
        <p>“My experience at Marlow Crest PT has been beyond terrific. All of the staff has been great and extremely friendly to deal with each week. I highly recommend Marlow Crest PT not only having a well educated staff but also a very pleasant environment!!!” - Dana Reyes</p>
      </div>
      <div class="bar" style="left:0;width:271px;justify-content:center;gap:7px">
        <svg width="12" height="12" viewBox="0 0 14 14" fill="none" stroke="currentColor" stroke-width="1.2"><circle cx="7" cy="7" r="6"/><ellipse cx="7" cy="7" rx="2.6" ry="6"/><path d="M1 7h12M2 4h10M2 10h10"/></svg>
        www.marlowcrestpt.example
      </div>
    </div>
  </section>

</div>
</body>
</html>
```